Book Cover design: Waltz with a Heron.

I need a front and back cover for my book called 'Waltz with a Heron'.
It is self development book for help a person to be a better coach.
It is a metaphor. Dance is asking questions and the octopus is the person you are coaching (complex with my 'tentacles').
The audience would be adults. so want the cover to capture attention and also show that is have something of interest inside.
I have attach my first attempt. Please be bold.
The best sellers in this market place have simple but clear front page & back pages.

All the words are important but the sub-title is likely to change.

Target Market(s)

Adults who work with each other.
More business type people.

Industry/Entity Type

Leadership

Font styles to use
Serif

Requirements
Must have
• My project must have... The words that in the draft mock up.
• 'Waltz with a Heron' [TITLE]
• 'A Path to True Mentoring'[SUB-TITLE]
• How to create inspiration and accountability using
• Seven Pivotal Turns.[SUB_TITLE]
• By Rowan P Thistlewood
Nice to have
• Clever and simple.

```html
<!DOCTYPE html>
<html lang="en">
<head>
<meta charset="utf-8">
<title>Waltz with a Heron — Book Cover</title>
<link rel="stylesheet" href="https://fonts.googleapis.com/css2?family=Jost:wght@300;400&family=Questrial&family=Cormorant+Garamond:wght@500;700&display=swap">
<style>
  :root{
    --paper:#fdfaf3;
    --title-orange:#c5532b;
    --title-navy:#2f4b68;
    --subtitle-maroon:#8e2f2c;
    --ink:#1b2430;
    --body-ink:#222;
    --sea-light:#cfe3ec;
    --sea-mid:#7fb3cc;
    --sea-deep:#3f86ab;
    --tentacle:#d2552c;
  }
  *{box-sizing:border-box;margin:0;padding:0}
  html,body{width:1200px;height:864px;overflow:hidden;background:var(--paper)}
  .cover{position:relative;width:1200px;height:864px;background:var(--paper);overflow:hidden}

  /* artwork */
  .sea{position:absolute;left:0;bottom:0;width:1200px;height:300px}
  .tentacle-art{position:absolute;border-radius:40% 60% 20% 20%;
    background:radial-gradient(ellipse at 50% 50%,rgba(210,85,44,.85),rgba(210,85,44,.35) 60%,rgba(210,85,44,0) 75%)}
  .tentacle-front{left:615px;top:420px;width:560px;height:320px}
  .tentacle-back{left:28px;top:622px;width:160px;height:110px}
  .dancer-art{position:absolute;left:1080px;top:350px;width:48px;height:82px;border-radius:20px;
    background:linear-gradient(#6c6f7d,#3e4050)}

  /* back cover */
  .blurb{position:absolute;left:48px;top:72px;width:513px;font-family:"Questrial",sans-serif;
    font-size:15.2px;line-height:19.4px;color:var(--body-ink);text-align:justify}
  .blurb p+p{margin-top:19px}
  .blurb p.tight{margin-top:0}
  .author-photo{position:absolute;left:48px;top:491px;width:139px;height:113px;background:#03060e}
  .author-bio{position:absolute;left:200px;top:489px;width:324px;font-family:"Questrial",sans-serif;
    font-size:14.2px;line-height:18.6px;color:var(--body-ink);text-align:justify}
  .author-bio strong{font-weight:400;color:#000}

  /* spine */
  .spine{position:absolute;left:582px;top:74px;width:34px;height:680px;writing-mode:vertical-rl;
    font-family:"Jost",sans-serif;font-weight:400;font-size:27px;letter-spacing:1px;white-space:nowrap}
  .spine-title{color:var(--title-orange)}
  .spine-title .accent{color:var(--title-navy)}
  .spine-author{position:absolute;top:434px;color:var(--ink)}

  /* front cover */
  .front{position:absolute;left:655px;top:58px;width:520px;text-align:center}
  .title-top{font-family:"Jost",sans-serif;font-weight:300;font-size:63px;line-height:70px;
    color:var(--title-orange);letter-spacing:1px}
  .title-main{font-family:"Jost",sans-serif;font-weight:300;font-size:108px;line-height:100px;
    color:var(--title-navy);letter-spacing:3px}
  .subtitle{margin-top:22px;font-family:"Cormorant Garamond",serif;font-weight:500;font-size:33px;
    color:var(--subtitle-maroon);letter-spacing:1.2px;text-transform:uppercase}
  .tagline{margin-top:10px;font-family:"Cormorant Garamond",serif;font-weight:500;font-size:15.5px;
    color:#444;letter-spacing:.8px;text-transform:uppercase}
  .tagline-key{font-family:"Cormorant Garamond",serif;font-weight:700;font-size:26px;color:#3a3a3a;
    letter-spacing:1.2px;text-transform:uppercase;line-height:28px}
  .author-front{position:absolute;left:655px;top:766px;width:520px;text-align:center;
    font-family:"Jost",sans-serif;font-weight:400;font-size:40px;color:var(--ink);letter-spacing:1px;
    text-transform:uppercase}
</style>
</head>
<body>
<main class="cover">

  <svg class="sea" viewBox="0 0 1200 300" preserveAspectRatio="none" role="img" aria-label="Painted blue sea surface stretching across both covers">
    <defs>
      <linearGradient id="seaFill" x1="0" y1="0" x2="0" y2="1">
        <stop offset="0" stop-color="var(--sea-light)"/>
        <stop offset=".35" stop-color="var(--sea-mid)"/>
        <stop offset="1" stop-color="var(--sea-deep)"/>
      </linearGradient>
    </defs>
    <path d="M0 135 C200 110 420 80 640 55 C820 30 1000 10 1200 0 L1200 300 L0 300 Z" fill="url(#seaFill)"/>
  </svg>

  <div class="tentacle-art tentacle-front" role="img" aria-label="Orange octopus tentacle curving up out of the sea"></div>
  <div class="tentacle-art tentacle-back" role="img" aria-label="Small octopus tentacle rising from the water"></div>
  <div class="dancer-art" role="img" aria-label="Dancer leaping on the tip of the tentacle"></div>

  <section class="back">
    <div class="blurb">
      <p>Tityre, tu patulae recubans sub tegmine fagi silvestrem tenui musam meditaris avena; nos patriae fines et dulcia linquimus arva; nos patriam fugimus: tu, Tityre, lentus in umbra formosam resonare doces Amaryllida silvas.</p>
      <p>O Meliboee, deus nobis haec otia fecit. Namque erit ille mihi semper deus; illius aram saepe tener nostris ab ovilibus imbuet agnus. Ille meas errare boves, ut cernis, et ipsum ludere quae vellem calamo permisit agresti.</p>
      <p>Non equidem invideo, miror magis: undique totis usque adeo turbatur agris. En ipse capellas protinus aeger ago; hanc etiam vix, Tityre, duco.</p>
      <p class="tight">Hic inter densas corylos modo namque gemellos, spem gregis, ah, silice in nuda conixa reliquit. Saepe malum hoc nobis, si mens non laeva fuisset, de caelo tactas memini praedicere quercus. Sed tamen iste deus qui sit da, Tityre, nobis.</p>
    </div>
    <div class="author-photo" role="img" aria-label="Author portrait placeholder"></div>
    <p class="author-bio"><strong>Rowan P Thistlewood</strong> e recubans sub tegmine fagi silvestrem tenui musam meditaris avena; nos patriae fines et dulcia linquimus arva; nos patriam fugimus: tu, Tityre, lentus in umbra formosam resonare doces Amaryllida silvas. musam meditaris avena; nos patriae fines et dulcia linquimus arva.</p>
  </section>

  <section class="spine">
    <span class="spine-title">WALTZ WITH A <span class="accent">HERON</span></span>
    <span class="spine-author">ROWAN P THISTLEWOOD</span>
  </section>

  <section class="front">
    <h1>
      <span class="title-top" style="display:block">WALTZ WITH A</span>
      <span class="title-main" style="display:block">HERON</span>
    </h1>
    <p class="subtitle">A Path to True Mentoring</p>
    <p class="tagline">How to create inspiration and accountability using</p>
    <p class="tagline-key">Seven Pivotal Turns</p>
  </section>

  <p class="author-front">Rowan P Thistlewood</p>
</main>
</body>
</html>
```